Virtualization software: PowerPoint, business cards

We're a young, small, dynamic application virtualization company: www.vorlint.com
We need a PowerPoint template + business cards. PDF background will be a plus.
This is mostly for enterprise clients.
Clean, professional, and most of all - following our website's colors.

Reason: Busy weekend; we'll need some more time to provide feedback & choose.

Corporate clients & investors.

Business

• Clean, professional, and following our website's look: www.vorlint.com

```html
<!DOCTYPE html>
<html lang="en">
<head>
<meta charset="utf-8">
<title>Vorlint – Business Cards &amp; Slide Template</title>
<link rel="stylesheet" href="https://fonts.googleapis.com/css2?family=Arimo:wght@400;700&display=swap">
<style>
  :root {
    --page: #ffffff;
    --card: #141414;
    --ink-light: #ffffff;
    --ink-muted: #c9c9c9;
    --accent: #8fd27a;
    --slide-bg: #f2f2f2;
    --slide-dark: #000000;
    --band-mid: #5a5a5a;
    --title: #000000;
    --subtitle: #808080;
  }
  * { margin: 0; padding: 0; box-sizing: border-box; }
  html, body { width: 900px; height: 1200px; overflow: hidden; background: var(--page); }
  body { position: relative; font-family: "Arimo", Arial, sans-serif; }

  .card {
    position: absolute; top: 107px; width: 424px; height: 270px;
    background: var(--card); border-radius: 14px; color: var(--ink-light);
  }
  .card--front { left: 11px; }
  .card--back { left: 453px; }

  .wordmark {
    position: absolute; font-weight: 400; color: var(--ink-light);
    line-height: 1; white-space: nowrap;
  }
  .card--front .wordmark {
    left: 0; right: 0; top: 112px; text-align: center;
    font-size: 46px; letter-spacing: 0.23em; padding-left: 0.23em;
  }
  .card--back .wordmark { left: 15px; top: 118px; font-size: 30px; letter-spacing: 0.24em; }

  .card__divider {
    position: absolute; left: 211px; top: 72px; width: 3px; height: 130px;
    background: linear-gradient(to bottom, transparent, var(--accent) 50%, transparent);
  }
  .card__details { position: absolute; left: 249px; top: 86px; }
  .card__name { font-size: 20px; font-weight: 700; }
  .card__role { margin-top: 16px; font-size: 12px; font-weight: 700; color: var(--ink-muted); }
  .card__small { font-size: 8px; font-weight: 700; color: var(--ink-muted); line-height: 9px; }
  .card__address { margin-top: 8px; }
  .card__contact { margin-top: 10px; }

  .slide {
    position: absolute; left: 0; top: 463px; width: 900px; height: 674px;
    background: var(--slide-bg); overflow: hidden;
  }
  .slide__header-band {
    position: absolute; left: 0; top: 0; width: 900px; height: 125px;
    background: linear-gradient(to bottom, var(--slide-dark) 0%, var(--slide-dark) 45%, var(--band-mid) 75%, var(--slide-bg) 100%);
  }
  .slide__title {
    position: absolute; right: 28px; top: 264px; font-size: 62px; font-weight: 700;
    color: var(--title); white-space: nowrap;
  }
  .slide__subtitle {
    position: absolute; right: 30px; top: 356px; font-size: 41.5px; font-weight: 700;
    color: var(--subtitle); white-space: nowrap;
  }
  .slide__footer {
    position: absolute; left: 0; bottom: 0; width: 900px; height: 27px;
    background: var(--slide-dark); color: var(--ink-light);
  }
  .slide__footer .wordmark { left: 11px; top: 4px; font-size: 20px; letter-spacing: 0.3em; }
  .slide__url { position: absolute; right: 22px; top: 5px; font-size: 15.5px; font-weight: 700; }
</style>
</head>
<body>
  <section class="card card--front" aria-label="Business card front">
    <span class="wordmark">VORLINT</span>
  </section>

  <section class="card card--back" aria-label="Business card back">
    <span class="wordmark">VORLINT</span>
    <div class="card__divider"></div>
    <div class="card__details">
      <p class="card__name">Dana Reyes</p>
      <p class="card__role">Job Title</p>
      <p class="card__small card__address">123 Address Street<br>Living City, 987654</p>
      <p class="card__small card__contact">dreyes@vorlint.com<br>www.vorlint.com</p>
    </div>
  </section>

  <section class="slide" aria-label="Title slide template">
    <div class="slide__header-band" role="img" aria-label="Decorative black and grey wave header"></div>
    <h1 class="slide__title">Click to add title</h1>
    <h2 class="slide__subtitle">Click to add subtitle</h2>
    <footer class="slide__footer">
      <span class="wordmark">VORLINT</span>
      <span class="slide__url">www.vorlint.com</span>
    </footer>
  </section>
</body>
</html>
```